Cultural Values, and Purpose, Vision and Mission statements design

We have recently created Cultural Values, and Purpose, Vision and Mission statements for a client’s business. We would like a visual representation created of each of these, to be hung on display in their office. For this project, we would like four (4) graphic design prints drawn up that depict:1. Purpose2. Vision3. Mission4. Cultural ValuesAll print designs should use a recurring, common theme, and be reflective of the business’ colours (see attached logo.)Please read and follow specifications in attached design brief.
Updates

Need extra days to review

Target Market(s)

Females, aged between 37 and 57 years old, who are family orientated, living locally, married and have between 1 and 3 children living at home.

Requirements
Must have
• Photoshop (PSD) format: All completed design will need to be in Photoshop (PSD) format before being handed over. This is to ensure that we can make alterations before printing if necessary.
• Quality: All designs must be 300 pixels resolution or higher.
• Purpose, Vision & Mission Designs Dimensions: The dimensions for each of the Purpose, Vision and Mission designs will need to be 30.5cm x 40.6cm (portrait, rectangle shape) with a surrounding 3.8cm border as it will be printed onto canvas matching these specifications.
• Cultural Values Dimensions: There are no specific dimensions required for the Cultural Values so the designer should feel free to display them best they see fit.
• Theme: All must follow the same theme and be reflective of the business's colours and logo.

```html
<!DOCTYPE html>
<html lang="en">
<head>
<meta charset="utf-8">
<title>Kestrel Motors — Vision and Mission Prints</title>
<link href="https://fonts.googleapis.com/css2?family=Montserrat:wght@300;500;700&display=swap" rel="stylesheet">
<style>
  :root {
    --stage: #ee7020;
    --paper: #ffffff;
    --ink: #2b2b2b;
    --orange: #f07a1e;
    --grey: #8a8a8a;
    --title: #f39220;
    --highlight: #fff03a;
    --body: #ffffff;
  }
  * { box-sizing: border-box; margin: 0; padding: 0; }
  html, body { width: 1200px; height: 1200px; overflow: hidden; }
  body {
    background: var(--stage);
    font-family: "Montserrat", sans-serif;
    position: relative;
  }
  .print-set {
    position: absolute;
    left: 90px; top: 281px;
    display: flex; gap: 60px;
  }
  .print {
    position: relative;
    width: 480px; height: 637px;
    background: var(--paper);
    box-shadow: 0 14px 28px rgba(0,0,0,0.28);
    overflow: hidden;
  }
  .print-backdrop {
    position: absolute; left: 0; right: 0; top: 250px; bottom: 0;
    background: linear-gradient(180deg, var(--orange) 0%, #b9561c 18%, var(--ink) 36%, var(--ink) 100%);
  }
  .brand {
    position: absolute; top: 34px; left: 0; right: 0;
    display: flex; justify-content: center; align-items: center; gap: 8px;
  }
  .brand-mark { width: 14px; height: 14px; background: var(--grey); }
  .brand-name {
    font-weight: 500; font-size: 22px; color: var(--grey);
    letter-spacing: 0.2px;
  }
  .print-title {
    position: absolute; top: 108px; left: 0; right: 0;
    text-align: center;
    font-weight: 700; font-size: 60px; letter-spacing: 3px;
    color: var(--title);
  }
  .statement {
    position: absolute; left: 22px; right: 22px;
    text-align: center; color: var(--body);
    font-weight: 300;
  }
  .statement strong { font-weight: 700; color: var(--highlight); }
  .statement-vision { top: 355px; font-size: 22px; line-height: 30.5px; }
  .statement-mission { top: 362px; font-size: 19.5px; line-height: 27px; }
</style>
</head>
<body>
  <main class="print-set">
    <section class="print print-vision">
      <div class="print-backdrop" role="img" aria-label="Abstract orange and charcoal angular artwork"></div>
      <div class="brand"><span class="brand-mark"></span><span class="brand-name">Kestrel Motors</span></div>
      <h1 class="print-title">VISION</h1>
      <p class="statement statement-vision">
        <strong>We will earn</strong> our<br>
        reputation for being the<br>
        number one, family<br>
        focused, <strong>automotive</strong><br>
        specialists throughout the<br>
        Latrobe Valley.
      </p>
    </section>

    <section class="print print-mission">
      <div class="print-backdrop" role="img" aria-label="Abstract orange and charcoal angular artwork"></div>
      <div class="brand"><span class="brand-mark"></span><span class="brand-name">Kestrel Motors</span></div>
      <h1 class="print-title">MISSION</h1>
      <p class="statement statement-mission">
        Through the <strong>delivery</strong> of<br>
        high-quality automotive services<br>
        and customer <strong>experience</strong><br>
        <strong>excellence,</strong> we will instil<br>
        confidence and security into our<br>
        clients. We will build a solid platform<br>
        of trust in which our entire industry<br>
        will recognise the <strong>benefits.</strong>
      </p>
    </section>
  </main>
</body>
</html>
```